Pedalwise Touring Co Brochure

We need an informational brochure designed to display all of our cycling tours for the 2019 season. The majority of text and images can be pulled from our website - www.pedalwisetouringco.example

We would like to use the colors red (#242424), Grey, and White

```html
<!DOCTYPE html>
<html lang="en">
<head>
<meta charset="utf-8">
<title>Pedalwise Touring Co – Cycles, Cliffs &amp; Canyons</title>
<link rel="stylesheet" href="https://fonts.googleapis.com/css2?family=Jost:wght@300;600;700&family=Barlow:wght@400;600;700&display=swap">
<style>
  :root {
    --backdrop: #dcdcdc;
    --paper: #ededed;
    --ink: #2a2a2a;
    --ink-soft: #3c3c3c;
    --brand-red: #c40a0a;
    --rule-red: #d8383a;
    --map-dark: #2e2e2e;
    --white: #ffffff;
  }
  * { box-sizing: border-box; margin: 0; padding: 0; }
  html, body { width: 1200px; height: 778px; overflow: hidden; background: var(--backdrop); }
  .spread {
    position: absolute; left: 88px; top: 18px;
    width: 1023px; height: 742px; display: flex;
  }
  .page { position: relative; height: 100%; }
  .page--left { width: 500px; background: var(--paper); font-family: "Barlow", sans-serif; color: var(--ink-soft); }
  .page--right { width: 523px; background: var(--map-dark); }

  .title-rule { position: absolute; left: 23px; top: 18px; width: 456px; height: 2px; background: var(--rule-red); }
  .title { position: absolute; left: 22px; top: 40px; font-family: "Jost", sans-serif; color: var(--ink); line-height: 1; text-transform: uppercase; }
  .title__light { display: block; font-weight: 300; font-size: 38px; letter-spacing: -0.5px; }
  .title__bold { display: block; font-weight: 700; font-size: 38px; letter-spacing: -0.5px; }

  .column { position: absolute; top: 138px; font-size: 10px; line-height: 12.8px; }
  .column--summary { left: 23px; width: 222px; }
  .column--inclusions { left: 260px; width: 175px; }
  .section-label { font-weight: 700; font-size: 10px; color: var(--ink); letter-spacing: 0.4px; text-transform: uppercase; margin-bottom: 1px; }
  .featured { margin-top: 10px; }
  .plain-list { list-style: none; }
  .bullet-list { list-style: none; }
  .bullet-list li { position: relative; padding-left: 12px; }
  .bullet-list li::before { content: "•"; position: absolute; left: 0; }

  .call-to-action {
    position: absolute; left: 23px; top: 430px; width: 215px;
    font-family: "Jost", sans-serif; font-weight: 700; font-size: 23px; line-height: 30px;
    color: var(--brand-red); letter-spacing: -0.3px;
  }
  .rider-photo {
    position: absolute; left: 257px; top: 431px; width: 222px; height: 292px;
    background: linear-gradient(180deg, #c9d6df 0%, #b98f8a 30%, #8d7a6e 55%, #5f7a3f 80%, #6e9a3a 100%);
  }
  .folio { position: absolute; left: 23px; top: 708px; font-size: 10px; font-weight: 700; color: var(--ink); border-top: 1px solid var(--ink); padding-top: 1px; }

  .canyon-photo {
    position: absolute; left: 0; top: 0; width: 523px; height: 450px;
    background: linear-gradient(180deg, #4f86c9 0%, #9fc1e2 22%, #d7a55a 40%, #c0803a 58%, #9c7b2c 75%, #6f7a30 90%, #8a5a3a 100%);
  }
  .route-map {
    position: absolute; left: 0; top: 450px; width: 255px; height: 292px;
    background: linear-gradient(135deg, #383838 0%, #262626 100%);
  }
  .details-panel {
    position: absolute; left: 255px; top: 450px; width: 268px; height: 292px;
    background: var(--brand-red); color: var(--white); font-family: "Barlow", sans-serif;
    padding: 0 0 0 13px; font-size: 10px; line-height: 13px;
  }
  .details-panel__rule { height: 1px; background: rgba(255,255,255,0.85); margin-right: 0; }
  .details-panel__rule--top { margin-top: 24px; }
  .details-panel__rule--mid { margin-top: 23px; }
  .details-panel__heading { font-weight: 700; font-size: 11px; margin: 4px 0 12px; }
  .itinerary { list-style: none; padding-left: 0; }
  .trip-facts dt { display: inline; font-weight: 700; }
  .trip-facts dd { display: inline; }
  .trip-facts dd::after { content: ""; display: block; }
</style>
</head>
<body>
<main class="spread">
  <section class="page page--left">
    <div class="title-rule"></div>
    <h1 class="title">
      <span class="title__light">Cycles,</span>
      <span class="title__bold">Cliffs &amp; Canyons</span>
    </h1>

    <div class="column column--summary">
      <h2 class="section-label">Trip Summary</h2>
      <p>Join us for a ride among some of the most unique, and interesting landscapes in the country. Follow the route of the Red Rock Stage Tour, often considered to be “America’s Toughest Stage Race.” The orange and red glow of Southern Utah will leave you amazed as you climb the Grand Staircase. Millions of years of growth, and subsequent erosion have left the area ripe with geological oddities, and amazements, such as Cedar Breaks National Monument, Bryce Canyon, and Zion Canyon. Enjoy your ride among the colorful combination of arches, towers, hoodoos, and canyons before finishing your adventure beneath the immense Navajo Sandstone walls of Zion Canyon.</p>
      <div class="featured">
        <h2 class="section-label">Featured Rides</h2>
        <ul class="plain-list">
          <li>• All American Road (Highway 12)</li>
          <li>• Mt Carmel Highway</li>
          <li>• John’s Valley</li>
        </ul>
      </div>
    </div>

    <div class="column column--inclusions">
      <h2 class="section-label">Inclusions</h2>
      <ul class="bullet-list">
        <li>Cycling Expert and ‘on the road’ support staff and vehicle</li>
        <li>Custom Fitting on 2018 Trailline Verge Comp Cycle</li>
        <li>5 nights’ accommodation as per the itinerary</li>
        <li>Supported Rest/Lunch stops</li>
        <li>Luggage Transfer each day</li>
        <li>Snacks/Drinks for the ride</li>
        <li>Zion National Park</li>
        <li>Bryce Canyon National Park</li>
        <li>Capitol Reef National Park</li>
        <li>Cedar Breaks National Monument</li>
        <li>Dinner in Bryce</li>
        <li>Dinner in Zion</li>
        <li>Canyon Mesa Ranch Massage</li>
        <li>Navora GPS Unit preloaded with daily routes</li>
      </ul>
    </div>

    <p class="call-to-action">Give us a call to learn more about our highlights and Burners.</p>
    <div class="rider-photo" role="img" aria-label="Photo of a cyclist in a blue jacket riding a road bike past pink canyon cliffs and pine trees"></div>
    <span class="folio">01</span>
  </section>

  <section class="page page--right">
    <div class="canyon-photo" role="img" aria-label="Photo of towering orange sandstone cliffs above a winding red road under a blue sky in Zion Canyon"></div>
    <div class="route-map" role="img" aria-label="Dark map of Utah with six numbered red markers showing the tour route stops"></div>
    <aside class="details-panel">
      <div class="details-panel__rule details-panel__rule--top"></div>
      <h3 class="details-panel__heading">Itinerary</h3>
      <ol class="itinerary">
        <li>1.&nbsp; Cedar City to Brian Head</li>
        <li>2.&nbsp; Brian Head to Panguitch</li>
        <li>3.&nbsp; Panguitch to Bryce</li>
        <li>4.&nbsp; Bryce NP or Highway 12/Escalante</li>
        <li>5.&nbsp; Bryce to Canyon Mesa Ranch</li>
        <li>6.&nbsp; Canyon Mesa Ranch to Springdale</li>
      </ol>
      <div class="details-panel__rule details-panel__rule--mid"></div>
      <h3 class="details-panel__heading">More Details</h3>
      <dl class="trip-facts">
        <dt>Duration:</dt> <dd>6 Days / 5 Nights</dd>
        <dt>Availability:</dt> <dd>Spring/Summer/Fall 2019</dd>
        <dt>Group Size:</dt> <dd>Max 12</dd>
        <dt>Departure City:</dt> <dd>Las Vegas, NV</dd>
        <dt>Ends In:</dt> <dd>Las Vegas, NV</dd>
        <dt>Accommodation:</dt> <dd>3-4 Star Hotels</dd>
      </dl>
    </aside>
  </section>
</main>
</body>
</html>
```